Harbor Crest Real Estate Business Cards

Looking to create a template for the agents in my office. The images below are an example of our current card, logos, and tagline. The requirements are:
1. Needs to include photo of agent
2. Needs to include Logo
3. Needs to include tag line. (current card doesn't include tagline.)
4. Needs to include phone, address, email, website and social media logos i.e. Find me at "f", "twitter (logo)" etc.
5. Need front and back design.
6. I don't want the old style safe style of business card. I want it to stand out in a stack of cards.
7. Do not make it look anything like what i currently have. This needs to be all new.
Thank you for your time.
Industry/Entity Type
Real Estate Agent
Contact Information for Business Card
I need name, address, email, website (www.pinevalleyhomefinder.example) social media logos
Requirements
Must have
- 1. Needs to include photo of agent
- 2. Needs to include Logo
- 3. Needs to include tag line. (current card doesn't include tagline.)
- 4. Needs to include phone, address, email, website and social media logos i.e. Find me at "f", "twitter (logo)" etc.
- 5. Need front and back design.
- 6. I don't want the old style safe style of business card. I want it to stand out in a stack of cards.
- 7. Do not make it look anything like what i currently have. This needs to be all new.
Should not have
- Not boring or plain.

```html
<!DOCTYPE html>
<html lang="en">
<head>
<meta charset="utf-8">
<title>Harbor Crest Real Estate – Business Card</title>
<link rel="stylesheet" href="https://fonts.googleapis.com/css2?family=Mulish:wght@400;600;700;800&display=swap">
<style>
  :root {
    --backdrop: #e4e2df;
    --card: #ffffff;
    --brand-red: #c8102e;
    --brand-grey: #6a6866;
    --text: #3f3f3f;
    --photo-top: #c9c6c2;
    --photo-bottom: #4a4b4f;
  }
  * { box-sizing: border-box; margin: 0; padding: 0; }
  html, body {
    width: 1200px; height: 1200px; overflow: hidden;
    background: var(--backdrop);
    font-family: "Mulish", Arial, sans-serif;
    color: var(--text);
  }
  .canvas { position: relative; width: 1200px; height: 1200px; }
  .card {
    position: absolute; left: 214px; width: 772px; height: 441px;
    background: var(--card);
    box-shadow: 0 6px 18px rgba(0,0,0,0.18);
    overflow: hidden;
  }
  .card--front { top: 150px; }
  .card--back { top: 633px; }

  .wordmark { color: var(--brand-grey); font-weight: 800; line-height: 1; }
  .wordmark__name { display: block; letter-spacing: -1px; }
  .wordmark__sub { display: block; text-align: right; letter-spacing: 3px; }

  .card--front .wordmark { position: absolute; left: 40px; top: 46px; width: 380px; }
  .card--front .wordmark__name { font-size: 46px; }
  .card--front .wordmark__sub { font-size: 18px; margin-top: 4px; }

  .agent { position: absolute; left: 40px; top: 158px; }
  .agent__name { color: var(--brand-red); font-weight: 700; font-size: 26px; letter-spacing: 0.5px; }
  .agent__title { font-size: 20px; margin-top: 4px; }
  .agent__address { font-size: 18px; line-height: 26px; margin-top: 20px; }
  .contact { list-style: none; margin-top: 10px; font-size: 18px; }
  .contact li { display: flex; align-items: center; height: 27px; }
  .contact svg { width: 16px; height: 16px; margin-right: 8px; flex: none; }

  .agent-photo {
    position: absolute; right: 0; top: 0; width: 320px; height: 441px;
    background: linear-gradient(180deg, var(--photo-top) 0%, var(--photo-bottom) 60%);
  }

  .card--back .wordmark { position: absolute; left: 118px; top: 146px; width: 540px; }
  .card--back .wordmark__name { font-size: 64px; }
  .card--back .wordmark__sub { font-size: 25px; margin-top: 4px; }
  .tagline {
    position: absolute; left: 0; right: 0; top: 255px; text-align: center;
    font-size: 28px; color: var(--brand-grey);
  }
  .social { position: absolute; left: 0; right: 0; top: 384px; display: flex; justify-content: center; gap: 6px; }
  .social span { width: 22px; height: 22px; background: var(--brand-red); border-radius: 4px; }
</style>
</head>
<body>
<main class="canvas">
  <section class="card card--front">
    <div class="wordmark">
      <span class="wordmark__name">HARBOR CREST</span>
      <span class="wordmark__sub">REAL ESTATE</span>
    </div>
    <div class="agent">
      <h1 class="agent__name">DANIEL WHITFORD</h1>
      <p class="agent__title">President &amp; CEO</p>
      <p class="agent__address">820 Alder Lane, Suite 300<br>Bayview, CA 94012</p>
      <ul class="contact">
        <li><svg viewBox="0 0 16 16" fill="none" stroke="#c8102e" stroke-width="1.4"><path d="M3 2l3 1 1 3-2 1a8 8 0 004 4l1-2 3 1 1 3-2 1C7 14 2 9 2 4z"/></svg>000-000-0000</li>
        <li><svg viewBox="0 0 16 16" fill="none" stroke="#c8102e" stroke-width="1.4"><rect x="4" y="1.5" width="8" height="13" rx="1.5"/><path d="M7 12h2"/></svg>000-000-0000</li>
        <li><svg viewBox="0 0 16 16" fill="none" stroke="#c8102e" stroke-width="1.4"><rect x="1.5" y="3.5" width="13" height="9"/><path d="M1.5 3.5L8 9l6.5-5.5"/></svg>info@pinevalleyhomefinder.example</li>
        <li><svg viewBox="0 0 16 16" fill="none" stroke="#c8102e" stroke-width="1.4"><circle cx="8" cy="8" r="6.5"/><path d="M1.5 8h13M8 1.5c-3 3.5-3 9.5 0 13M8 1.5c3 3.5 3 9.5 0 13"/></svg>www.pinevalleyhomefinder.example</li>
      </ul>
    </div>
    <div class="agent-photo" role="img" aria-label="Portrait photo of the agent in a dark suit"></div>
  </section>

  <section class="card card--back">
    <div class="wordmark">
      <span class="wordmark__name">HARBOR CREST</span>
      <span class="wordmark__sub">REAL ESTATE</span>
    </div>
    <p class="tagline">Where Every Door Leads You Home</p>
    <div class="social" aria-label="Social media links">
      <span></span><span></span><span></span><span></span>
    </div>
  </section>
</main>
</body>
</html>
```